Clark County Assessor Canditate

We need a billboard ad for a political candidate Tessa Harrow who is running for Clark County Assessor in an upcoming election. Needs to be simple and to the point to get the people to see the name "Tessa Harrow" and what to vote for "Clark County Assessor" in Las Vegas, NV. Also the billboard visibility is best in the top side of the sign, so the information should be most prominent in the top right, middle, left sides.The size of the billboard is 14 ft Height X 48 ft Wide Also needs some bright colors that are noticable from a freeway viewed billboard.Designers - I need to have "Paid for by Tessa Harrow for Clark County Assessor" on the sign
I have uploaded a few headshots you can work with to create a design. Thank you,

http://tessaharrow-vote.info/

Voters

Political

• Name, what I am voting for, and some image that represents Las Vegas and/or Nevada

```html
<!DOCTYPE html>
<html lang="en">
<head>
<meta charset="utf-8">
<title>Vote Tessa Harrow for Clark County Assessor</title>
<link rel="stylesheet" href="https://fonts.googleapis.com/css2?family=Open+Sans:wght@600;800&family=Anton&display=swap">
<style>
  :root {
    --stage: #8c8c8c;
    --red: #e10000;
    --blue: #005196;
    --dark: #1d1d1d;
    --dark-soft: #2e2d2c;
    --white: #ffffff;
    --map-grey: #d4d4d4;
  }
  html, body {
    margin: 0;
    padding: 0;
    width: 1200px;
    height: 569px;
    overflow: hidden;
    background: var(--stage);
  }
  .billboard {
    position: absolute;
    left: 50px;
    top: 50px;
    width: 1101px;
    height: 439px;
    overflow: hidden;
    background: var(--dark);
  }
  .candidate-photo {
    position: absolute;
    left: 0;
    top: 0;
    width: 560px;
    height: 439px;
    background: radial-gradient(ellipse at 45% 45%, #c9a978 0%, #7a6346 28%, var(--dark-soft) 55%, var(--dark) 100%);
  }
  .panels {
    position: absolute;
    inset: 0;
  }
  .state-map {
    position: absolute;
    left: 552px;
    top: 30px;
    width: 158px;
    height: 96px;
    background: var(--map-grey);
    border-radius: 6px;
  }
  .headline {
    position: absolute;
    right: 51px;
    margin: 0;
    color: var(--white);
    font-family: "Open Sans", sans-serif;
    white-space: nowrap;
    line-height: 1;
  }
  .headline-vote {
    top: 43px;
    font-size: 76px;
    font-weight: 800;
  }
  .headline-name {
    top: 129px;
    font-size: 80px;
    font-weight: 800;
    letter-spacing: -0.5px;
  }
  .office-for {
    top: 256px;
    font-size: 42px;
    font-weight: 600;
  }
  .office-location {
    top: 368px;
    font-size: 27px;
    font-weight: 600;
  }
  .disclaimer {
    top: 420px;
    font-size: 12px;
    font-weight: 600;
  }
  .office-title {
    position: absolute;
    left: 0;
    top: 0;
    width: 1101px;
    height: 439px;
  }
  .office-title text {
    fill: var(--white);
    font-family: "Anton", sans-serif;
    font-size: 51px;
  }
</style>
</head>
<body>
  <main class="billboard">
    <div class="candidate-photo" role="img" aria-label="Headshot of the candidate Tessa Harrow against a dark studio backdrop"></div>

    <svg class="panels" width="1101" height="439" viewBox="0 0 1101 439" aria-hidden="true">
      <polygon points="362,0 1101,0 1101,439 542,439" fill="var(--red)"/>
      <polygon points="778,0 1101,0 1101,123 828,123" fill="var(--blue)"/>
      <polygon points="414,234 1101,234 1101,413 485,413" fill="var(--blue)"/>
    </svg>

    <div class="state-map" role="img" aria-label="Map of the United States with Nevada highlighted"></div>

    <p class="headline headline-vote">VOTE</p>
    <h1 class="headline headline-name">Tessa Harrow</h1>
    <p class="headline office-for">FOR</p>

    <svg class="office-title" viewBox="0 0 1101 439" aria-label="Clark County Assessor">
      <text x="1050" y="350" text-anchor="end" textLength="542" lengthAdjust="spacingAndGlyphs">CLARK COUNTY ASSESSOR</text>
    </svg>

    <p class="headline office-location">Las Vegas, NV.</p>
    <p class="headline disclaimer">Paid for by Tessa Harrow for Clark County Assessor</p>
  </main>
</body>
</html>
```